New Body Mist 250 ml exclusive

We are excited to embark on a new project to design the packaging for body mist:
Lunar Bramble

We are looking for a design that is truly unique and stands out, with a touch of individuality that sets it apart. The design should be eye-catching and visually appealing, drawing attention even from a distance. We want the body mists to have a fun and attractive look that appeals to customers.

To help bring your design to life, we will provide the dimensions of the bottle, which has a capacity of 250ml. The bottle measures 13.3 cm in height and 4.9 cm in diameter (excluding the pump). Additionally, we will also provide the dimensions of the label, which measures 15.1 cm in height and 12.8 cm in width.

We believe that giving you the freedom to put your own unique touch and color choices will help create a truly standout design. We look forward to seeing your creative vision for our body mist.

We shared with you the logo of the body mist and some examples of models that we liked.

Please be informed that the project only includes one design and the remaining three will be completed and paid for through a 1on1 project with the winner of the contest.

Target Market(s)

Supermarket and perfumery stores

Industry/Entity Type

Cosmetics

Font styles to use
Serif

Requirements
Must have
• Uniqueness and attractiveness

```html
<!DOCTYPE html>
<html lang="en">
<head>
<meta charset="utf-8">
<title>Lunar Bramble – Moonlit Reverie Body Mist Label</title>
<link href="https://fonts.googleapis.com/css2?family=Cinzel:wght@500;600;700&display=swap" rel="stylesheet">
<style>
  :root {
    --page: #ffffff;
    --label-bg: #f4eff9;
    --lilac-soft: #e3d9f6;
    --lilac-mid: #c9b6ef;
    --ink: #141014;
    --gold-dark: #b87b1e;
    --gold-mid: #d9a941;
    --gold-light: #f6e6b4;
  }
  * { margin: 0; padding: 0; box-sizing: border-box; }
  html, body {
    width: 1200px; height: 1200px; overflow: hidden;
    background: var(--page);
  }
  .canvas {
    position: relative; width: 1200px; height: 1200px;
    font-family: "Cinzel", "Times New Roman", serif;
    color: var(--ink);
  }
  .label {
    position: absolute; left: 362px; top: 40px;
    width: 475px; height: 1120px;
    background: var(--label-bg);
    overflow: hidden;
  }
  .gold-rule {
    position: absolute; left: 0; width: 100%; height: 3px;
    background: linear-gradient(90deg, var(--gold-dark), var(--gold-mid) 40%, var(--gold-light) 80%, var(--gold-mid));
  }
  .rule-1 { top: 32px; }
  .rule-2 { top: 51px; }
  .rule-3 { top: 1060px; }
  .rule-4 { top: 1080px; }

  .mandala-crest {
    position: absolute; left: 87px; top: 83px;
    width: 300px; height: 300px; border-radius: 50%;
    background: radial-gradient(circle, var(--lilac-soft) 0%, #ebe3f8 55%, rgba(244,239,249,0) 72%);
  }
  .brand-name {
    position: absolute; left: 0; top: 205px; width: 100%;
    text-align: center;
    font-size: 38px; font-weight: 600; letter-spacing: 4px;
    text-transform: uppercase;
    color: var(--ink);
  }

  .gold-band {
    position: absolute; left: 0; top: 420px; width: 100%; height: 182px;
    background: linear-gradient(90deg, var(--gold-dark) 0%, var(--gold-mid) 25%, var(--gold-light) 50%, var(--gold-mid) 75%, var(--gold-dark) 100%);
    text-align: center;
    text-transform: uppercase;
  }
  .scent-name {
    position: absolute; left: 0; top: 38px; width: 100%;
    font-size: 34px; font-weight: 600; letter-spacing: 0.5px;
    line-height: 40px;
  }
  .product-type {
    position: absolute; left: 0; top: 76px; width: 100%;
    font-size: 66px; font-weight: 700; letter-spacing: 1px;
    line-height: 76px;
  }

  .splash-art {
    position: absolute; left: 0; top: 602px; width: 100%; height: 450px;
    background:
      radial-gradient(ellipse 55% 60% at 65% 35%, var(--lilac-soft) 0%, rgba(227,217,246,0.6) 60%, rgba(244,239,249,0) 100%),
      radial-gradient(ellipse 40% 55% at 5% 55%, rgba(201,182,239,0.55) 0%, rgba(244,239,249,0) 100%);
  }
  .tagline {
    position: absolute; left: 0; top: 752px; width: 100%;
    text-align: center;
    font-size: 32px; font-weight: 600; line-height: 40px;
    text-transform: uppercase;
  }
  .volume {
    position: absolute; left: 0; top: 1012px; width: 100%;
    text-align: center;
    font-size: 26px; font-weight: 600; letter-spacing: 1px;
  }
</style>
</head>
<body>
  <main class="canvas">
    <section class="label">
      <div class="gold-rule rule-1"></div>
      <div class="gold-rule rule-2"></div>

      <div class="mandala-crest" role="img" aria-label="Lilac line-drawn mandala with radiating dashes behind the brand name"></div>
      <h1 class="brand-name">Lunar Bramble</h1>

      <div class="gold-band">
        <p class="scent-name">Moonlit Reverie</p>
        <p class="product-type">Body Mist</p>
      </div>

      <div class="splash-art" role="img" aria-label="Soft lilac watercolour splash with a partial mandala on the left edge"></div>
      <p class="tagline">Soothing<br>Quiet Orchards</p>
      <p class="volume">250ml / 8 fl oz</p>

      <div class="gold-rule rule-3"></div>
      <div class="gold-rule rule-4"></div>
    </section>
  </main>
</body>
</html>
```